Australian small vineyard seeking wine label.

We need a wine label design for a new wine brand \Boutique winery - 2 vintages so far, looking for something a little eye catching, but simple.
Wine label name: Harlow and Co
2013 Cabernet Shiraz
2014 Shiraz
Estate grown
Vineyard located at Sevenhill in the Clare valley South Australia.

Target Market(s)

ladies aged between 20 and 50

Industry/Entity Type

Boutique

Logo Text

Harlow and Co

Logo styles of interest
Emblem Logo
Pictorial/Combination Logo
Abstract Logo
Character Logo
Font styles to use
Serif
Script

Requirements
Must have
• easy to read text
Nice to have
• The grape grower and winemaker is Martin Harlow -
• had some thoughts of Captain Brindle - Australian - naval flag
• But very open to ideas
Should not have
• over complications and colors due to cost of wine label being determined by amount of colors required abd print set up.

```html
<!DOCTYPE html>
<html lang="en">
<head>
<meta charset="utf-8">
<title>Harlow and Co — Shiraz 2014 Labels</title>
<link rel="stylesheet" href="https://fonts.googleapis.com/css2?family=Cinzel:wght@400;500&family=Cormorant+Garamond:wght@500&display=swap">
<style>
  :root {
    --backdrop: #d9d9d9;
    --cream: #ede3c6;
    --wine-red: #7e0a0e;
    --charcoal: #262626;
    --ink: #3a2f28;
    --paper-white: #f3efe6;
    --sketch-cream: #c9bda0;
    --sketch-grey: #5c5c5c;
  }
  * { margin: 0; padding: 0; box-sizing: border-box; }
  html, body {
    width: 1200px;
    height: 800px;
    overflow: hidden;
    background: var(--backdrop);
  }
  .label-pair {
    width: 1200px;
    height: 800px;
    display: flex;
    align-items: center;
    justify-content: center;
    gap: 60px;
  }
  .label {
    width: 500px;
    height: 360px;
    display: flex;
    flex-direction: column;
    box-shadow: 0 6px 18px rgba(0,0,0,0.18);
  }
  .label__band {
    height: 78px;
    display: flex;
    align-items: center;
    justify-content: center;
  }
  .label__brand {
    font-family: "Cinzel", serif;
    font-weight: 500;
    font-size: 38px;
    letter-spacing: 2px;
  }
  .label__body {
    flex: 1;
    display: flex;
    flex-direction: column;
    align-items: center;
    padding-top: 22px;
  }
  .label__ship {
    width: 190px;
    height: 118px;
    border-radius: 4px;
  }
  .label__variety {
    font-family: "Cinzel", serif;
    font-size: 34px;
    letter-spacing: 7px;
    margin-top: 14px;
    line-height: 1;
  }
  .label__vintage {
    font-family: "Cormorant Garamond", serif;
    font-weight: 500;
    font-size: 18px;
    letter-spacing: 1px;
    margin-top: 8px;
  }
  .label__estate {
    font-family: "Cinzel", serif;
    font-size: 15px;
    letter-spacing: 1px;
    margin-top: 12px;
  }
  .label__origin {
    font-family: "Cinzel", serif;
    font-size: 11px;
    letter-spacing: 1px;
    margin-top: 6px;
  }

  /* Red band edition */
  .label--red .label__band { background: var(--wine-red); }
  .label--red .label__brand { color: var(--paper-white); }
  .label--red .label__body { background: var(--cream); color: var(--ink); }

  /* Black edition */
  .label--black .label__band { background: var(--cream); }
  .label--black .label__brand { color: var(--wine-red); }
  .label--black .label__body { background: var(--charcoal); color: var(--paper-white); }
</style>
</head>
<body>
  <main class="label-pair">
    <section class="label label--red">
      <header class="label__band">
        <span class="label__brand">Harlow and Co</span>
      </header>
      <div class="label__body">
        <svg class="label__ship" role="img" aria-label="Pen sketch of a three-masted sailing ship on the sea" viewBox="0 0 190 118">
          <defs>
            <linearGradient id="shipCream" x1="0" y1="0" x2="0" y2="1">
              <stop offset="0" stop-color="#ddd2b4"/>
              <stop offset="1" stop-color="#c4b795"/>
            </linearGradient>
          </defs>
          <rect width="190" height="118" rx="4" fill="url(#shipCream)"/>
        </svg>
        <h1 class="label__variety">SHIRAZ</h1>
        <p class="label__vintage">2014</p>
        <p class="label__estate">Estate Grown</p>
        <p class="label__origin">Sevenhill&nbsp; Clare Valley South Australia</p>
      </div>
    </section>

    <section class="label label--black">
      <header class="label__band">
        <span class="label__brand">Harlow and Co</span>
      </header>
      <div class="label__body">
        <svg class="label__ship" role="img" aria-label="White line sketch of a three-masted sailing ship on the sea" viewBox="0 0 190 118">
          <defs>
            <linearGradient id="shipGrey" x1="0" y1="0" x2="0" y2="1">
              <stop offset="0" stop-color="#4a4a4a"/>
              <stop offset="1" stop-color="#3a3a3a"/>
            </linearGradient>
          </defs>
          <rect width="190" height="118" rx="4" fill="url(#shipGrey)"/>
        </svg>
        <h2 class="label__variety">SHIRAZ</h2>
        <p class="label__vintage">2014</p>
        <p class="label__estate">Estate Grown</p>
        <p class="label__origin">Sevenhill&nbsp; Clare Valley South Australia</p>
      </div>
    </section>
  </main>
</body>
</html>
```